" Trata-se de uma construtora em conjunto com um escritório de engenharia e arquitetura para prestar serviços de construção, gerenciamento de obras e projetos e desenho. "

```html
<!DOCTYPE html>
<html lang="pt-BR">
<head>
<meta charset="UTF-8">
<title>Norvia — Construindo Sonhos</title>
<link href="https://fonts.googleapis.com/css2?family=Montserrat:wght@500;600;700;800&display=swap" rel="stylesheet">
<style>
  :root {
    --nav-bg: #2b2d31;
    --nav-text: #e6e6e6;
    --accent: #f5c518;
    --headline: #ffffff;
    --sky-top: #4a4f5c;
    --sky-mid: #c98a4a;
    --sun: #f3a640;
    --city-dark: #2c2a2e;
    --page-bg: #1e1f22;
  }
  * { margin: 0; padding: 0; box-sizing: border-box; }
  html, body {
    width: 1200px;
    height: 1200px;
    overflow: hidden;
    background: var(--page-bg);
    font-family: "Montserrat", sans-serif;
  }
  .site {
    position: relative;
    width: 1200px;
    height: 1200px;
  }
  .topbar {
    position: absolute;
    top: 0; left: 0; right: 0;
    height: 84px;
    background: var(--nav-bg);
    display: flex;
    align-items: center;
    justify-content: space-between;
    padding: 0 48px;
    z-index: 2;
  }
  .brand {
    display: flex;
    align-items: center;
    gap: 10px;
    color: var(--accent);
    font-weight: 700;
    font-size: 20px;
    letter-spacing: 2px;
  }
  .brand-dot {
    width: 14px; height: 14px;
    border-radius: 50%;
    background: var(--accent);
  }
  .menu {
    display: flex;
    align-items: center;
    gap: 40px;
    list-style: none;
  }
  .menu-item {
    color: var(--nav-text);
    font-size: 15px;
    font-weight: 600;
    letter-spacing: 1.5px;
  }
  .menu-item.is-active { color: var(--accent); }
  .social {
    display: flex;
    gap: 12px;
    margin-left: 12px;
  }
  .social-dot {
    width: 14px; height: 14px;
    border-radius: 50%;
    background: var(--accent);
  }
  .hero {
    position: absolute;
    top: 84px; left: 0; right: 0; bottom: 0;
    background:
      radial-gradient(ellipse 55% 35% at 28% 52%, rgba(255,196,90,0.85), rgba(243,166,64,0) 70%),
      linear-gradient(180deg, var(--sky-top) 0%, #8a6e5c 28%, var(--sky-mid) 48%, #7a5a48 68%, var(--city-dark) 100%);
  }
  .hero-content {
    position: absolute;
    top: 300px;
    left: 0; right: 0;
    text-align: center;
  }
  .headline {
    color: var(--headline);
    font-weight: 800;
    font-size: 92px;
    letter-spacing: 1px;
    line-height: 1.05;
  }
  .tagline {
    color: var(--headline);
    font-weight: 700;
    font-size: 64px;
    line-height: 1.2;
    margin-top: 6px;
  }
  .tagline-accent { color: var(--accent); }
  .scroll-cue {
    display: block;
    margin: 60px auto 0;
  }
</style>
</head>
<body>
  <main class="site">
    <header class="topbar">
      <div class="brand"><span class="brand-dot"></span>NORVIA</div>
      <nav>
        <ul class="menu">
          <li class="menu-item is-active">HOME</li>
          <li class="menu-item">NORVIA</li>
          <li class="menu-item">O QUE FAZEMOS</li>
          <li class="menu-item">SOBRE NÓS</li>
          <li class="menu-item">CONTATO</li>
          <li class="social">
            <span class="social-dot"></span>
            <span class="social-dot"></span>
            <span class="social-dot"></span>
          </li>
        </ul>
      </nav>
    </header>

    <section class="hero" role="img" aria-label="Fotografia de uma cidade com arranha-céus ao pôr do sol, céu dourado e prédios em primeiro plano">
      <div class="hero-content">
        <h1 class="headline">WE BUILD BRASIL</h1>
        <p class="tagline">Construíndo <span class="tagline-accent">Sonhos</span></p>
        <svg class="scroll-cue" width="72" height="72" viewBox="0 0 72 72" aria-hidden="true">
          <circle cx="36" cy="36" r="33" fill="none" stroke="#ffffff" stroke-width="3"/>
          <line x1="36" y1="20" x2="36" y2="50" stroke="#ffffff" stroke-width="4" stroke-linecap="round"/>
          <polyline points="24,40 36,52 48,40" fill="none" stroke="#ffffff" stroke-width="4" stroke-linecap="round" stroke-linejoin="round"/>
        </svg>
      </div>
    </section>
  </main>
</body>
</html>
```